依頼詳細
【コンテンツ】
基本的なコンテンツは、現在のページ https://korvane.jp/ を元に構成してください。
・[制作実績] ですが、[制作実績 - ホームページ] と [制作実績 - システム開発] に分けて頂き、それぞれ簡単な説明テキスト「○○○…」とイメージ画像などがあると良いかもしれません(ブロック内の正方形のサンプル画像はそのままご使用頂いても [No Photo] 等で代替して頂いても結構です)。
・[お知らせ] と [お問い合わせはこちら] の間に [よくあるご質問] のブロックを追加してください(テキストは「○○○…」で結構です)。
・その他、企業サイトによくあるようなコンテンツで おすすめのコンテンツがございましたら デザイン内にてご提案頂けますと幸いです。

【レイアウト】
・レイアウトは(現状2カラムになってますが)1カラムで構成して頂いても結構です。おすすめのレイアウトでお願いいたします(バナー広告は不要です)。
・幅は1366pxでお願いいたします(最近見かけます画面一杯に広がっているレイアウトはあまり好みではありません。背景画像が画面一杯に広がっているのは構いませんが、コンテンツは中央よりに配置したいと思います。後ほど弊社にてレスポンシブにコーディングする予定です)。
・グローバルメニューは現状の6メニューでお願いいたします。フッターメニューは常時差し替えが発生しますので「○○○」などで代替して頂いて結構です。

【配色・デザイン等】
・配色としては モノトーン(黒)を基調として頂き、見出し背景色などもモノトーンでも結構ですし、あえて一色挙げるとしますと #405080 (HSV 225度 - 50% -50%) などのネイビーまたは青などのクールな色味が好みです。その他のアイキャッチ画像やコンテンツ等の色味は単色でもカラフルなものでも結構です。ブリッカー様のセンスにお任せしたいと思います。
・ロゴマークは先日 Brikka で依頼したものですので、変更せずにそのままご使用ください。
・アイキャッチ等の写真画像は、弊社で Pelmora Images をライセンス契約しておりますので、Pelmora Images のサンプル画像をご使用頂き、別途 画像のURLを当選後にお知らせ頂けましたら結構です。
・アイキャッチ画像のイメージ(内容)ですが、弊社のサービスは 主軸サービス(バックエンド)として (1)システム開発 があり、集客用サービス(フロントエンド)として (2)ホームページ制作 があります。これらのサービスを総合すると (1) を構成する お客様の「笑顔」と弊社の「誠実さ」との「信頼関係」(人間性)がベースとなり、その上に (2) のホームページ制作(デジタルITサービス)が存在する…といったイメージになると思います。それら2つを、例えば半透明にして手前と奥で重ね合わせる/上下にレイアウトする/2枚の画像を JavaScript でアニメーション化するなどは、ブリッカー様のセンスにてお願いできましたらと思います(弊社にてコーディングしますのでご提案ください)。
サイトURL
https://korvane.jp/
ページ数
1ページ
希望イメージ
シンプル 複雑
単色 カラフル
暗い 明るい
日常 高級
遊び心 厳粛
未来的 伝統的
女性的 男性的
希望する色
青系、水色系、グレー系
納品ファイル
• フォトショップ形式 (.psd)
補足説明
Adobe Photoshop CC *psd 形式で、レイヤーを分けて制作・納品頂けますと幸いです。
予想していたよりも提案件数が少なかったので、少し内容をシンプルにして 期間を延長させて頂きました。変更箇所とその他印象等は 以下の通りでございますので、何卒よろしくお願い申し上げます。

【依頼詳細の変更】
・アイキャッチ画像のイメージ(内容)ですが「パソコンで仕事をしている人の笑顔」が含まれている画像でしたらどんなものでも結構です。(すでにご提案頂いているものにつきましては修正して頂かなくても結構です)
・「How to enjoy creative work?」というテキストは入れて頂かない方が良いかと思います(そこまで重要視しておりませんので)。
・見出しテキスト(「制作実績」「お知らせ」など)は左寄せの方が好みです。
・全体の配色ですが、カラフルな感じより 白を基調としたモノトーンな感じの方が好みです。
・[お問い合わせはこちら] ですが、今後 他のページ(ランディングページ)などにも挿入していく可能性がありますので、バナーっぽく制作頂けますと有り難いです。

白を基調としたシンプルなレイアウトで、ディテールまで洗練されていたデザインでしたので 一目見て気に入って選ばせて頂きました。
テンプレートでのデザインが主流になりつつある中、テンプレートでは表現できないような個性のあるものになったのではないかと思いまして 大変満足しております。ありがとうございました。

皆様に個別に御礼メッセージをお送りすることはできませんでしたが、予想以上の大変多くのご提案をご応募頂けまして大変満足しております。本当にありがとうございました。また機会がございましたら 何卒よろしくお願い申し上げます。

```html
<!DOCTYPE html>
<html lang="ja">
<head>
<meta charset="utf-8">
<title>Korvane | ホームページ制作・システム開発</title>
<link rel="stylesheet" href="https://fonts.googleapis.com/css2?family=Noto+Sans+JP:wght@400;500;700&family=Montserrat:wght@400;500;600&display=swap">
<style>
  :root {
    --ink: #1a1a1a;
    --text: #333333;
    --muted: #8a8a8a;
    --line: #dcdcdc;
    --faint: #ececec;
    --bg: #f3f3f3;
    --panel: #ffffff;
    --thumb: #e4e4e4;
    --banner: #111111;
  }
  * { box-sizing: border-box; margin: 0; padding: 0; }
  html, body { width: 1200px; height: 2832px; overflow: hidden; }
  body {
    position: relative;
    font-family: "Noto Sans JP", sans-serif;
    color: var(--text);
    background-color: var(--bg);
    background-image:
      repeating-linear-gradient(90deg, transparent 0 199px, var(--faint) 199px 200px),
      repeating-linear-gradient(0deg, transparent 0 199px, var(--faint) 199px 200px);
  }
  .en { font-family: "Montserrat", sans-serif; letter-spacing: .08em; }

  /* Header */
  .site-header { position: absolute; top: 0; left: 0; width: 1200px; height: 112px; background: var(--panel); }
  .brand { position: absolute; left: 56px; top: 44px; display: flex; align-items: center; gap: 10px; }
  .brand-square { width: 14px; height: 14px; background: var(--ink); }
  .brand-name { font-size: 24px; font-weight: 500; color: var(--ink); letter-spacing: .02em; }
  .global-nav { position: absolute; right: 40px; top: 46px; display: flex; }
  .global-nav a {
    display: block; padding: 0 22px; border-left: 1px solid var(--line);
    text-decoration: none; color: var(--ink);
  }
  .global-nav a:last-child { border-right: 1px solid var(--line); }
  .global-nav .ja { display: block; font-size: 13px; font-weight: 500; }
  .global-nav .en { display: block; font-size: 8px; color: var(--muted); margin-top: 3px; }

  /* Hero */
  .hero {
    position: absolute; top: 112px; left: 40px; width: 1120px; height: 588px;
    background: linear-gradient(120deg, #3a3a3a 0%, #8c8c8c 35%, #d8d8d8 55%, #9a9a9a 75%, #2e2e2e 100%);
    clip-path: polygon(0 0, 34% 0, 50% 7%, 66% 0, 100% 0, 100% 100%, 0 100%);
  }

  /* Shared section */
  .panel { position: absolute; left: 40px; width: 1120px; background: var(--panel); }
  .section-title { position: absolute; left: 48px; top: 36px; }
  .section-title h2 { font-size: 24px; font-weight: 700; color: var(--ink); }
  .section-title .en { display: block; font-size: 8px; color: var(--muted); margin-top: 4px; }
  .section-title::after { content: ""; display: block; width: 24px; height: 2px; background: var(--ink); margin-top: 6px; }
  .more-btn {
    position: absolute; width: 72px; height: 18px; border: 1px solid var(--ink);
    font-size: 8px; text-align: center; line-height: 16px; color: var(--ink);
  }

  /* Works */
  .works { top: 740px; height: 520px; }
  .works-group { position: absolute; top: 112px; width: 476px; }
  .works-group.web { left: 48px; }
  .works-group.system { left: 596px; }
  .works-group h3 { font-size: 14px; font-weight: 500; color: var(--ink); padding-bottom: 10px; border-bottom: 1px solid var(--ink); }
  .works-group .more-btn { right: 0; top: -2px; }
  .work-cards { display: flex; gap: 28px; margin-top: 26px; }
  .work-card { width: 224px; }
  .work-thumb { width: 224px; height: 176px; background: var(--thumb); }
  .work-client { font-size: 10px; color: var(--muted); margin-top: 16px; }
  .work-name { font-size: 13px; font-weight: 500; color: var(--ink); margin-top: 2px; }
  .work-desc { font-size: 10px; color: var(--muted); line-height: 1.7; margin-top: 8px; }

  /* News */
  .news { top: 1320px; height: 420px; }
  .news .more-btn { right: 48px; top: 88px; }
  .news-list { position: absolute; left: 48px; top: 130px; width: 1024px; list-style: none; border-top: 1px solid var(--line); }
  .news-list li { display: flex; height: 66px; align-items: center; border-bottom: 1px solid var(--line); font-size: 12px; }
  .news-list time { width: 150px; padding-left: 16px; color: var(--muted); font-family: "Montserrat", sans-serif; font-size: 11px; }

  /* FAQ */
  .faq { top: 1840px; height: 480px; }
  .faq-list { position: absolute; left: 48px; top: 120px; width: 1024px; list-style: none; border: 1px solid var(--line); }
  .faq-list li { position: relative; display: flex; align-items: center; height: 48px; border-bottom: 1px solid var(--line); font-size: 12px; font-weight: 500; color: var(--ink); }
  .faq-list li:last-child { border-bottom: none; }
  .faq-q { width: 44px; text-align: center; font-family: "Montserrat", sans-serif; font-size: 16px; font-weight: 600; }
  .faq-plus { position: absolute; right: 18px; top: 17px; }

  /* Contact banner */
  .contact-banner {
    position: absolute; left: 40px; top: 2472px; width: 1120px; height: 136px;
    background: var(--banner); color: #fff; text-align: center; text-decoration: none;
  }
  .contact-banner .ja { display: block; font-size: 22px; font-weight: 500; padding-top: 46px; }
  .contact-banner .en { display: block; font-size: 8px; color: #aaa; margin-top: 6px; }
  .contact-banner svg { position: absolute; right: 44px; top: 56px; }

  /* Scroll top */
  .scroll-line { position: absolute; left: 600px; top: 2608px; width: 1px; height: 108px; background: var(--ink); }
  .scroll-top { position: absolute; left: 540px; top: 2716px; width: 120px; height: 26px; border: 1px solid var(--ink); background: var(--panel); font-size: 9px; text-align: center; line-height: 24px; color: var(--ink); }

  /* Footer */
  .site-footer { position: absolute; left: 0; top: 2768px; width: 1200px; height: 64px; display: flex; justify-content: space-between; align-items: center; padding: 0 40px; }
  .footer-nav { display: flex; gap: 18px; font-size: 11px; color: var(--text); }
  .copyright { font-size: 9px; color: var(--muted); }
</style>
</head>
<body>

<header class="site-header">
  <div class="brand"><span class="brand-square"></span><span class="brand-name">Korvane</span></div>
  <nav class="global-nav">
    <a href="#"><span class="ja">ホームページ制作</span><span class="en">WEB DESIGN</span></a>
    <a href="#"><span class="ja">システム開発</span><span class="en">SYSTEM DEVELOPMENT</span></a>
    <a href="#"><span class="ja">料金表</span><span class="en">PRICE</span></a>
    <a href="#"><span class="ja">会社概要</span><span class="en">COMPANY</span></a>
    <a href="#"><span class="ja">お問い合わせ</span><span class="en">CONTACT</span></a>
  </nav>
</header>

<div class="hero" role="img" aria-label="パソコンを囲んで打ち合わせをする笑顔のスタッフのモノクロ写真"></div>

<section class="panel works">
  <div class="section-title"><h2>制作実績</h2><span class="en">WORKS</span></div>

  <div class="works-group web">
    <h3>ホームページ制作</h3>
    <span class="more-btn en">VIEW MORE</span>
    <div class="work-cards">
      <article class="work-card">
        <div class="work-thumb" role="img" aria-label="No Photo サンプル画像"></div>
        <p class="work-client">株式会社ソラノ</p>
        <p class="work-name">コーポレートサイト</p>
        <p class="work-desc">新しいブランドに合わせた企業サイトを<br>設計し、更新しやすい構成で制作しました。</p>
      </article>
      <article class="work-card">
        <div class="work-thumb" role="img" aria-label="No Photo サンプル画像"></div>
        <p class="work-client">株式会社ソラノ</p>
        <p class="work-name">コーポレートサイト</p>
        <p class="work-desc">新しいブランドに合わせた企業サイトを<br>設計し、更新しやすい構成で制作しました。</p>
      </article>
    </div>
  </div>

  <div class="works-group system">
    <h3>システム開発</h3>
    <span class="more-btn en">VIEW MORE</span>
    <div class="work-cards">
      <article class="work-card">
        <div class="work-thumb" role="img" aria-label="No Photo サンプル画像"></div>
        <p class="work-client">株式会社ソラノ</p>
        <p class="work-name">本部展開型業務システム</p>
        <p class="work-desc">複数拠点の業務を一元管理できる仕組みを<br>設計し、運用まで一貫して担当しました。</p>
      </article>
      <article class="work-card">
        <div class="work-thumb" role="img" aria-label="No Photo サンプル画像"></div>
        <p class="work-client">株式会社ソラノ</p>
        <p class="work-name">本部展開型業務システム</p>
        <p class="work-desc">複数拠点の業務を一元管理できる仕組みを<br>設計し、運用まで一貫して担当しました。</p>
      </article>
    </div>
  </div>
</section>

<section class="panel news">
  <div class="section-title"><h2>お知らせ</h2><span class="en">INFORMATION</span></div>
  <span class="more-btn en">VIEW ALL</span>
  <ul class="news-list">
    <li><time>2019.12.30</time><span>年末年始休業は12月28日から1月5日までとさせていただきます。</span></li>
    <li><time>2019.12.30</time><span>ホームページ制作の料金表をリニューアルしました。</span></li>
    <li><time>2019.12.30</time><span>システム開発の新しい導入事例を公開しました。</span></li>
    <li><time>2019.12.30</time><span>会社概要ページを更新し、アクセス情報を追加しました。</span></li>
  </ul>
</section>

<section class="panel faq">
  <div class="section-title"><h2>よくある質問</h2><span class="en">FAQ</span></div>
  <ul class="faq-list">
    <li><span class="faq-q">Q</span>○○○○○○○○○○○○○○○○○○○○○○○○○○○○○○○○○○○○○○○○○○○○<svg class="faq-plus" width="12" height="12" viewBox="0 0 12 12"><path d="M6 0v12M0 6h12" stroke="#1a1a1a" stroke-width="1"/></svg></li>
    <li><span class="faq-q">Q</span>○○○○○○○○○○○○○○○○○○○○○○○○○○○○○○○○○○○○○○○○○○○○<svg class="faq-plus" width="12" height="12" viewBox="0 0 12 12"><path d="M6 0v12M0 6h12" stroke="#1a1a1a" stroke-width="1"/></svg></li>
    <li><span class="faq-q">Q</span>○○○○○○○○○○○○○○○○○○○○○○○○○○○○○○○○○○○○○○○○○○○○<svg class="faq-plus" width="12" height="12" viewBox="0 0 12 12"><path d="M6 0v12M0 6h12" stroke="#1a1a1a" stroke-width="1"/></svg></li>
    <li><span class="faq-q">Q</span>○○○○○○○○○○○○○○○○○○○○○○○○○○○○○○○○○○○○○○○○○○○○<svg class="faq-plus" width="12" height="12" viewBox="0 0 12 12"><path d="M6 0v12M0 6h12" stroke="#1a1a1a" stroke-width="1"/></svg></li>
    <li><span class="faq-q">Q</span>○○○○○○○○○○○○○○○○○○○○○○○○○○○○○○○○○○○○○○○○○○○○<svg class="faq-plus" width="12" height="12" viewBox="0 0 12 12"><path d="M6 0v12M0 6h12" stroke="#1a1a1a" stroke-width="1"/></svg></li>
    <li><span class="faq-q">Q</span>○○○○○○○○○○○○○○○○○○○○○○○○○○○○○○○○○○○○○○○○○○○○<svg class="faq-plus" width="12" height="12" viewBox="0 0 12 12"><path d="M6 0v12M0 6h12" stroke="#1a1a1a" stroke-width="1"/></svg></li>
    <li><span class="faq-q">Q</span>○○○○○○○○○○○○○○○○○○○○○○○○○○○○○○○○○○○○○○○○○○○○<svg class="faq-plus" width="12" height="12" viewBox="0 0 12 12"><path d="M6 0v12M0 6h12" stroke="#1a1a1a" stroke-width="1"/></svg></li>
  </ul>
</section>

<a class="contact-banner" href="#">
  <span class="ja">お問い合わせ</span>
  <span class="en">INQUIRY</span>
  <svg width="14" height="24" viewBox="0 0 14 24"><path d="M1 1l11 11L1 23" fill="none" stroke="#ffffff" stroke-width="1.5"/></svg>
</a>

<div class="scroll-line"></div>
<div class="scroll-top en">SCROLL TOP</div>

<footer class="site-footer">
  <nav class="footer-nav">
    <span>トップ</span><span>ホームページ制作</span><span>システム開発</span><span>料金表</span><span>会社概要</span><span>お問い合わせ</span>
  </nav>
  <p class="copyright en">Copyright © Korvane Inc. All rights reserved.</p>
</footer>

</body>
</html>
```